Redesign Home Page

We need a new home page with a white background. Our company provides singing instruction to students world wide, both in person and on line. We're looking for a very clean and open design with maximum white space. The main goal of the page will be to get users to sign up for our mailing list. The current site is www.kelvarsong.com. I think the new page can be a long page (scrolll down is ok), to allow for more white space while still using the text from the current page.
Updates

Project Deadline Extended
Reason: Hello to all Designers, I apologize for not giving feedback this weekend. We went out of town for the Memorial Day holiday and I had no internet. I will be extending the deadline to Thursday. -Marcus

Target Market(s)

Singers of all ages and abilities, especially beginners.

Industry/Entity Type

It Company

Requirements
Must have
• 1. A white background
2. Lots of open space
3. An email sign up form on the top right that reads:
a. “Improve Your Singing Now.
b. Sign up for our Free Video Series: Tone Pathway
4. Testimonails: found on https://www.kelvarsong.com/tone-ascent
5. My logo with the piano
6. My photo
7. Learn about our Lessons in:
a. San Francisco
b. Alameda
8. On Line Programs:
a. Tone Ascent
b. Zelvo Lessons

Nice to have
• Link to current student page: http://kelvarsong.com/what-students-say/students2
Pictures of singers
Video box: Use Marcus_Example
Should not have
• See "KelvarSong Redesign" file for more details.

```html
<!DOCTYPE html>
<html lang="en">
<head>
<meta charset="utf-8">
<title>MarcusKelvar School of Voice</title>
<link rel="stylesheet" href="https://fonts.googleapis.com/css2?family=Open+Sans:wght@300;400;600;700&family=Roboto+Condensed:wght@400;700&family=Raleway:wght@300;400&family=Caveat:wght@400&display=swap">
<style>
:root{
  --blue:#2aa5dd;
  --blue-dark:#1c8cc0;
  --ink:#222;
  --text:#555;
  --muted:#888;
  --line:#e2e2e2;
  --band:#f3f3f3;
  --footer:#1f1f1f;
  --footer-deep:#161616;
  --white:#fff;
}
*{box-sizing:border-box;margin:0;padding:0}
html,body{width:1200px;height:4260px;overflow:hidden;background:var(--white)}
body{font-family:"Open Sans",Arial,sans-serif;color:var(--text);font-size:13px;line-height:1.55;position:relative}
a{color:inherit;text-decoration:none}
.section{position:absolute;left:0;width:1200px}
.heading{font-family:"Roboto Condensed",Arial,sans-serif;font-weight:700;font-size:30px;color:var(--ink);text-transform:uppercase;text-align:center;letter-spacing:.5px}
.heading em{font-style:normal;color:var(--blue)}
.heading-rule{width:60px;height:2px;background:var(--blue);margin:14px auto 0}
.btn{display:inline-block;background:var(--blue);color:var(--white);font-family:"Roboto Condensed",Arial,sans-serif;font-weight:700;font-size:13px;text-transform:uppercase;padding:8px 16px;letter-spacing:.5px}
.placeholder{position:absolute}

/* Header */
.site-header{top:0;height:142px;border-bottom:1px solid var(--line)}
.brand{position:absolute;left:36px;top:22px;display:flex;align-items:center;gap:12px}
.brand-dot{width:48px;height:48px;border-radius:50%;background:var(--blue)}
.brand-name{font-family:"Open Sans",sans-serif;font-weight:700;font-size:28px;color:var(--ink);line-height:1}
.brand-sub{font-size:14px;color:var(--muted);margin-top:4px}
.signup{position:absolute;right:30px;top:14px;width:370px}
.signup-title{font-family:"Roboto Condensed",sans-serif;font-weight:700;font-size:12px;color:var(--ink);text-transform:uppercase;margin-bottom:8px}
.signup-grid{display:grid;grid-template-columns:1fr 1fr;gap:8px}
.signup-field{border:1px solid #ccc;height:28px;font-size:11px;color:#999;padding:5px 8px}
.signup-submit{height:28px;background:var(--blue);color:var(--white);font-size:11px;font-weight:600;text-align:center;padding-top:6px}
.main-nav{position:absolute;left:36px;top:106px;display:flex;font-family:"Roboto Condensed",sans-serif;font-weight:700;font-size:14px;color:var(--ink);text-transform:uppercase}
.main-nav a{padding:0 14px;border-left:1px solid #ccc;line-height:16px;height:16px}
.main-nav a:first-child{border-left:0;padding-left:0;color:var(--blue)}
.main-nav a.active{position:relative}
.main-nav a.active::after{content:"";position:absolute;left:0;right:14px;top:30px;height:3px;background:var(--blue)}

/* Hero */
.hero{top:142px;height:622px;border-bottom:1px solid var(--line)}
.hero-photo{left:0;top:0;width:600px;height:622px;background:linear-gradient(100deg,#2b2b2b 0%,#6a6a6a 45%,#cfcfcf 80%,#ffffff 100%)}
.hero-copy{position:absolute;left:640px;top:92px;width:500px;font-family:"Raleway",sans-serif;font-weight:300;font-size:31px;line-height:1.38;color:var(--ink)}
.hero-copy em{font-style:normal;color:var(--blue);font-weight:400}
.hero-play{position:absolute;left:612px;top:250px}
.hero-cta{position:absolute;left:700px;top:368px;font-family:"Caveat",cursive;font-size:38px;color:var(--ink)}

/* Welcome */
.welcome{top:815px;height:250px;text-align:center}
.welcome p{width:1100px;margin:34px auto 0;font-size:13px;color:var(--text)}

/* Advantages */
.advantages{top:1100px;height:590px;background:var(--band)}
.advantages .heading{margin-top:40px}
.adv-photo{left:440px;top:130px;width:320px;height:460px;background:linear-gradient(180deg,#e8e8e8 0%,#b9a69a 40%,#4a3030 75%,#2e2626 100%)}
.adv-col{position:absolute;top:150px;width:370px}
.adv-col.left{left:36px}
.adv-col.right{left:800px}
.feature{margin-bottom:40px}
.feature h3{font-family:"Roboto Condensed",sans-serif;font-weight:700;font-size:20px;color:var(--ink);margin-bottom:8px}
.feature h3 em{font-style:normal;color:var(--blue)}
.feature p{font-size:12px;color:var(--text);line-height:1.6}

/* Locations */
.locations{top:1740px;height:700px}
.location{position:absolute;top:90px;width:540px}
.location.alameda{left:36px}
.location.sanfran{left:624px}
.loc-city{font-family:"Roboto Condensed",sans-serif;font-weight:700;font-size:22px;color:var(--blue);line-height:1}
.loc-addr{font-size:12px;color:var(--text);margin-top:4px}
.loc-email{position:absolute;right:0;top:4px;padding:6px 16px}
.loc-photo{position:relative;margin-top:14px;width:540px;height:195px}
.loc-photo.day{background:linear-gradient(180deg,#8dc7ea 0%,#cfe6f2 55%,#8a9aa8 70%,#4a6676 100%)}
.loc-photo.night{background:linear-gradient(180deg,#3a2a6a 0%,#8a4a8e 45%,#e2a06a 65%,#2a2236 100%)}
.loc-meta{display:flex;gap:120px;margin-top:18px;font-size:12px}
.loc-meta b{display:block;color:var(--ink)}
.loc-body{margin-top:16px;font-size:12px;line-height:1.6}
.loc-instructor{margin-top:10px;font-size:12px;color:var(--ink);font-weight:600}
.loc-instructor span{color:var(--blue);font-weight:400}

/* Online programs */
.programs{top:2485px;height:560px;border-top:1px solid var(--line);padding-top:50px}
.programs .intro{width:1100px;margin:30px auto 0;text-align:center;font-size:12px}
.program{position:absolute;top:235px;width:540px}
.program.ascent{left:36px}
.program.zelvo{left:624px}
.program-art{position:absolute;left:0;top:0;width:210px;height:180px}
.program-art.ascent-art{background:linear-gradient(135deg,#12345a 0%,#1f6aa3 55%,#8bc9ea 100%)}
.zelvo-mark{position:absolute;left:10px;top:10px;width:200px;height:160px;display:flex;align-items:center;gap:12px}
.zelvo-dot{width:100px;height:100px;border-radius:50%;background:var(--blue)}
.zelvo-name{font-size:24px;font-weight:700;color:var(--blue)}
.program-info{position:absolute;left:240px;top:0;width:300px}
.program-info h3{font-family:"Roboto Condensed",sans-serif;font-weight:700;font-size:19px;color:var(--ink);margin-bottom:12px}
.program-info p{font-size:12px;line-height:1.6}
.program-info p a{color:var(--blue)}
.program-info .btn{margin-top:18px;font-size:12px;padding:7px 14px}

/* Testimonials */
.clients{top:3085px;height:430px;border-top:1px solid var(--line);padding-top:38px}
.testimonial{position:absolute;top:160px;width:350px}
.testimonial:nth-of-type(1){left:36px}
.testimonial:nth-of-type(2){left:425px}
.testimonial:nth-of-type(3){left:814px}
.avatar{position:absolute;left:0;top:0;width:100px;height:100px;background:linear-gradient(160deg,#d9c4b4 0%,#8a6a5a 60%,#3e302a 100%)}
.t-body{margin-left:118px}
.t-name{font-family:"Roboto Condensed",sans-serif;font-weight:700;font-size:17px;color:var(--ink);line-height:1}
.t-city{font-size:11px;color:var(--muted);margin:3px 0 12px}
.t-quote{font-size:12px;line-height:1.55}

/* Promo */
.promo{top:3515px;height:296px}
.promo-photo{left:36px;top:0;width:300px;height:296px;background:linear-gradient(180deg,#ffffff 0%,#9a9a9a 35%,#3a3a3a 100%)}
.promo-signature{left:200px;top:250px;width:120px;height:30px;background:linear-gradient(90deg,#eeeeee,#d6d6d6)}
.promo-text{position:absolute;left:360px;top:50px;width:360px;font-size:12px;line-height:1.6}
.promo-text a{color:var(--blue)}
.promo-video{left:745px;top:30px;width:395px;height:235px;background:linear-gradient(160deg,#0d1e3a 0%,#1b3f73 55%,#0a1528 100%)}
.promo-play{position:absolute;left:912px;top:117px}

/* Consult bar */
.consult{top:3811px;height:80px;background:var(--blue);color:var(--white)}
.consult h2{position:absolute;left:36px;top:14px;font-family:"Roboto Condensed",sans-serif;font-weight:700;font-size:27px;text-transform:uppercase;line-height:1.1}
.consult p{position:absolute;left:36px;top:50px;font-size:12px}
.consult .btn{position:absolute;right:36px;top:20px;background:#1a1a1a;padding:11px 22px;font-size:14px}

/* Footer */
.site-footer{top:3891px;height:318px;background:var(--footer);color:#bbb}
.footer-cols{position:absolute;left:36px;top:30px;width:1128px;display:flex;gap:40px}
.footer-col{width:252px}
.footer-col h4{font-family:"Roboto Condensed",sans-serif;font-weight:700;font-size:14px;color:var(--white);text-transform:uppercase;margin-bottom:10px}
.footer-lists{display:flex;gap:30px}
.footer-lists ul{list-style:none;font-size:12px;line-height:1.75}
.touch{position:absolute;left:0;top:168px;width:1200px;display:flex;align-items:center;justify-content:center;gap:22px}
.touch span.rule{width:440px;height:1px;background:#444}
.touch h4{font-family:"Roboto Condensed",sans-serif;font-weight:700;font-size:22px;color:var(--white);text-transform:uppercase}
.contact-row{position:absolute;left:36px;top:226px;width:1128px;display:flex;justify-content:space-between}
.contact-item{display:flex;gap:12px;align-items:flex-start;width:360px}
.contact-item b{display:block;font-family:"Roboto Condensed",sans-serif;color:var(--white);font-size:14px;text-transform:uppercase}
.contact-item span{font-size:12px}
.copyright{top:4209px;height:51px;background:var(--footer-deep);color:#999;font-size:12px}
.copyright p{position:absolute;left:36px;top:16px}
.social{position:absolute;right:36px;top:12px;display:flex;gap:8px}
.social i{display:block;width:26px;height:26px;border-radius:50%;background:#555}
.social i:nth-child(1){background:#3d5e9c}
.social i:nth-child(2){background:var(--blue)}
.social i:nth-child(3){background:#d34836}
.social i:nth-child(4){background:#e07a22}
.social i:nth-child(5){background:#c4302b}
</style>
</head>
<body>

<header class="section site-header">
  <div class="brand">
    <span class="brand-dot"></span>
    <div>
      <div class="brand-name">MarcusKelvar</div>
      <div class="brand-sub">School of Voice</div>
    </div>
  </div>
  <form class="signup">
    <div class="signup-title">Signup for our voice programs</div>
    <div class="signup-grid">
      <div class="signup-field">User Name</div>
      <div class="signup-field">Email address</div>
      <div class="signup-field">Password</div>
      <div class="signup-submit">Create an Account</div>
    </div>
  </form>
  <nav class="main-nav">
    <a class="active" href="#">Home</a>
    <a href="#">Voice Lessons</a>
    <a href="#">Blog</a>
    <a href="#">What Students Say</a>
    <a href="#">Meet the Instructors</a>
    <a href="#">Tone Ascent</a>
    <a href="#">Contact</a>
  </nav>
</header>

<section class="section hero">
  <div class="placeholder hero-photo" role="img" aria-label="Black and white portrait photo of vocal coach Marcus D. Kelvar"></div>
  <p class="hero-copy">Professional vocal coach, <em>Marcus D. Kelvar</em> has laid the vocal foundation for thousands of singers worldwide, for <em>20+ years.</em></p>
  <svg class="hero-play" width="90" height="90" viewBox="0 0 90 90" aria-hidden="true">
    <circle cx="45" cy="45" r="42" fill="none" stroke="#2aa5dd" stroke-width="4"/>
    <circle cx="45" cy="45" r="34" fill="#2aa5dd"/>
    <path d="M37 30 L61 45 L37 60 Z" fill="#fff"/>
  </svg>
  <svg style="position:absolute;left:640px;top:340px" width="70" height="60" viewBox="0 0 70 60" aria-hidden="true">
    <path d="M66 48 C40 50 18 36 10 6" fill="none" stroke="#222" stroke-width="2"/>
    <path d="M4 14 L10 4 L17 13" fill="none" stroke="#222" stroke-width="2"/>
  </svg>
  <div class="hero-cta">Watch Video Now!</div>
</section>

<section class="section welcome">
  <h2 class="heading">Welcome to <em>MarcusKelvar School of Voice</em></h2>
  <div class="heading-rule"></div>
  <p>The MarcusKelvar School of Voice offers state of the art voice instruction in San Francisco, Alameda, and on line. We love working with beginners and professionals, so whether you're just starting to explore singing or are an experienced performing vocalist looking to perfect your singing technique, we can help.</p>
</section>

<section class="section advantages">
  <h2 class="heading">Advantages of working with <em>Tone Ascent</em></h2>
  <div class="heading-rule"></div>
  <div class="placeholder adv-photo" role="img" aria-label="Photo of a young woman singing into a microphone"></div>
  <div class="adv-col left">
    <div class="feature"><h3>Flexibility is <em>Paramount</em></h3><p>Learn at the pace that suits your week, with lessons you can schedule around work, school and family life without losing any progress.</p></div>
    <div class="feature"><h3>Downloadable <em>Content</em></h3><p>Every lesson can be saved to your device, so you can warm up and practise your exercises anywhere, even with no connection.</p></div>
    <div class="feature"><h3>Adaptable <em>Course Format</em></h3><p>Mix private lessons, video modules and live sessions into a plan that fits your voice, your goals and your current level.</p></div>
  </div>
  <div class="adv-col right">
    <div class="feature"><h3>Personal <em>Interaction</em></h3><p>Get direct feedback on your recordings and ask questions along the way, so you always know what to work on next.</p></div>
    <div class="feature"><h3>Vocal <em>Health Education</em></h3><p>Understand how to protect your voice, avoid strain and keep your instrument healthy for a lifetime of confident singing.</p></div>
    <div class="feature"><h3>Vocal <em>Foundation</em></h3><p>Build breath support, pitch control and resonance step by step, creating a solid base that every style of music can grow from.</p></div>
  </div>
</section>

<section class="section locations">
  <h2 class="heading">Which location works <em>best for you?</em></h2>
  <div class="location alameda">
    <div class="loc-city">Alameda</div>
    <div class="loc-addr">Near Bayview and Alder</div>
    <a class="btn loc-email" href="#">Email Us</a>
    <div class="placeholder loc-photo day" role="img" aria-label="Photo of a sunny marina with sailboats in Alameda"></div>
    <div class="loc-meta">
      <div><b>Hours :</b>Monday to Friday 1:00 PM to 8:00 PM<br>Saturday 12:00 PM to 4:00 PM</div>
      <div><b>Call Us :</b>510.555.0147</div>
    </div>
    <p class="loc-body">This venue has a beautiful private studio equipped with a digital recording and video production capabilities. We offer private one on one voice lessons and producing. Whether you're just starting out and learning the basics or seasoned professional preparing for your next release, Marcus is available to help you.</p>
    <div class="loc-instructor">Instructor: <span>Marcus Kelvar</span></div>
  </div>
  <div class="location sanfran">
    <div class="loc-city">San Francisco</div>
    <div class="loc-addr">410 Larch ST #115</div>
    <a class="btn loc-email" href="#">Email Us</a>
    <div class="placeholder loc-photo night" role="img" aria-label="Photo of the San Francisco bay and bridge at dusk"></div>
    <div class="loc-meta">
      <div><b>Hours :</b>Tuesday 12:00 PM to 9:00 PM<br>Thursday 12:00 PM to 9:00 PM</div>
      <div><b>Call Us :</b>415.555.0192</div>
    </div>
    <p class="loc-body">Located downtown near the Harbor Arts Center, the studio is equipped with a 9 foot grand piano and all lessons are recorded onto CD. Parking is close by, or take the train to Larch Street Station. The studio is just a short walk from there.</p>
    <div class="loc-instructor">Instructor: <span>Marcus Kelvar</span></div>
  </div>
</section>

<section class="section programs">
  <h2 class="heading">MarcusKelvar <em>Online Programs</em></h2>
  <div class="heading-rule"></div>
  <p class="intro">Can't make it to a studio? Our online programs bring the same proven method to your home, with video lessons, live sessions and practice tracks you can use at any time.<br>Choose the format that suits you best and start improving your singing today, wherever you are in the world.</p>
  <div class="program ascent">
    <div class="placeholder program-art ascent-art" role="img" aria-label="Tone Ascent DVD video series product set"></div>
    <div class="program-info">
      <h3>Tone Ascent</h3>
      <p>Tone Ascent is a Video Series designed to give you all the techniques you need to fully develop your singing voice. With 30 videos, sixty audio workouts, and an eBook, the platform is the most advanced you'll find anywhere. <a href="#">Click here for more information</a>.</p>
      <a class="btn" href="#">Purchase Now</a>
    </div>
  </div>
  <div class="program zelvo">
    <div class="zelvo-mark"><span class="zelvo-dot"></span><span class="zelvo-name">Zelvo</span></div>
    <div class="program-info">
      <h3>Zelvo Lessons</h3>
      <p>About half of Marcus's students work with him using Zelvo. It's nearly as effective as an in person lesson, and you'll be provided with an MP3 recording of the lesson right away so you can get started practicing your singing technique immediately.</p>
      <a class="btn" href="#">Live Chat Now</a>
    </div>
  </div>
</section>

<section class="section clients">
  <h2 class="heading">What about <em>clients says</em></h2>
  <div class="heading-rule"></div>
  <div class="testimonial">
    <div class="placeholder avatar" role="img" aria-label="Student portrait photo"></div>
    <div class="t-body">
      <div class="t-name">SEROFTING MARCUS</div>
      <div class="t-city">San Francisco</div>
      <p class="t-quote">My range grew so much in just a few months. The lessons are clear and fun, and I finally sing with real confidence on stage.</p>
    </div>
  </div>
  <div class="testimonial">
    <div class="placeholder avatar" role="img" aria-label="Student portrait photo"></div>
    <div class="t-body">
      <div class="t-name">SEROFTING MARCUS</div>
      <div class="t-city">San Francisco</div>
      <p class="t-quote">My range grew so much in just a few months. The lessons are clear and fun, and I finally sing with real confidence on stage.</p>
    </div>
  </div>
  <div class="testimonial">
    <div class="placeholder avatar" role="img" aria-label="Student portrait photo"></div>
    <div class="t-body">
      <div class="t-name">SEROFTING MARCUS</div>
      <div class="t-city">San Francisco</div>
      <p class="t-quote">My range grew so much in just a few months. The lessons are clear and fun, and I finally sing with real confidence on stage.</p>
    </div>
  </div>
</section>

<section class="section promo">
  <div class="placeholder promo-photo" role="img" aria-label="Black and white portrait photo of Marcus Kelvar"></div>
  <div class="placeholder promo-signature" role="img" aria-label="Handwritten signature of Marcus Kelvar"></div>
  <p class="promo-text">I believe in Tone Ascent wholeheartedly, and I want you to be fully satisfied with the program. That's why I stand behind Tone Ascent with a 100% money back guarantee. I am confident that by making this small investment now, you will learn the keys to achieving having a breakthrough with your voice. <a href="#">Click here for more information</a>.</p>
  <div class="placeholder promo-video" role="img" aria-label="Tone Ascent video preview"></div>
  <svg class="promo-play" width="60" height="60" viewBox="0 0 60 60" aria-hidden="true">
    <circle cx="30" cy="30" r="28" fill="#2aa5dd"/>
    <path d="M24 18 L42 30 L24 42 Z" fill="#fff"/>
  </svg>
</section>

<section class="section consult">
  <h2>Free consultation with Marcus</h2>
  <p>Marcus Kelvar has openings for a free 15 minute consultation over the phone if you have questions about your voice.</p>
  <a class="btn" href="#">Click here to set up your time slot</a>
</section>

<footer class="section site-footer">
  <div class="footer-cols">
    <div class="footer-col">
      <h4>Quick Links</h4>
      <div class="footer-lists">
        <ul><li>Home</li><li>Voice Lessons</li><li>Blog</li><li>What Students Say</li></ul>
        <ul><li>Meet the Instructors</li><li>Tone Ascent</li><li>Contact</li></ul>
      </div>
    </div>
    <div class="footer-col">
      <h4>Other Links</h4>
      <div class="footer-lists">
        <ul><li>About Us</li><li>Support</li><li>KelvarSong</li><li>FAQ</li></ul>
        <ul><li>Privacy Policy</li><li>Terms of use</li><li>Sitemap</li></ul>
      </div>
    </div>
    <div class="footer-col">
      <h4>Online Program</h4>
      <div class="footer-lists"><ul><li>Tone Ascent</li><li>Zelvo Lessons</li></ul></div>
    </div>
    <div class="footer-col">
      <h4>About Lessons</h4>
      <div class="footer-lists"><ul><li>San Francisco</li><li>Alameda</li></ul></div>
    </div>
  </div>
  <div class="touch"><span class="rule"></span><h4>Get in touch</h4><span class="rule"></span></div>
  <div class="contact-row">
    <div class="contact-item">
      <svg width="30" height="30" viewBox="0 0 30 30" aria-hidden="true"><path d="M8 4 L12 4 L14 10 L11 12 C12 15 15 18 18 19 L20 16 L26 18 L26 22 C26 24 24 26 22 26 C13 25 5 17 4 8 C4 6 6 4 8 4 Z" fill="#2aa5dd"/></svg>
      <div><b>Phone Number</b><span>(800) 555 01 2468</span></div>
    </div>
    <div class="contact-item">
      <svg width="30" height="30" viewBox="0 0 30 30" aria-hidden="true"><rect x="3" y="7" width="24" height="16" fill="none" stroke="#2aa5dd" stroke-width="2"/><path d="M3 7 L15 17 L27 7" fill="none" stroke="#2aa5dd" stroke-width="2"/></svg>
      <div><b>Email Us</b><span>info@marcuskelvarvoice.com</span></div>
    </div>
    <div class="contact-item">
      <svg width="30" height="30" viewBox="0 0 30 30" aria-hidden="true"><rect x="5" y="4" width="20" height="23" fill="none" stroke="#2aa5dd" stroke-width="2"/><path d="M9 10 H21 M9 15 H21 M9 20 H17" stroke="#2aa5dd" stroke-width="2"/></svg>
      <div><b>Contact Form</b><span>Click here to use Contact Form.</span></div>
    </div>
  </div>
</footer>

<div class="section copyright">
  <p>© 2014 KelvarSong.com. All Rights Reserved</p>
  <div class="social"><i></i><i></i><i></i><i></i><i></i></div>
</div>

</body>
</html>
```